Unique, Impressive, and Modern Business Card

Looking for a distinctive, unique business card. We are distributors of tire repairs supplies, tools, machinery, and chemicals. Our target market are tire repair shops, tire franchises, and mechanic shops. We would like our design to include tire characteristics, and use our business colors. Feel free to use all types design and printing options (emboss, spot uv, foil, etc) QR code may be applied, you can use different size business cards ( standard, square, rounded edge, colored edge, etc), all formats needed for printing, also editable for future changes

Target Market(s)

Automotive, Tire industries

Industry/Entity Type

Tire Industry (automotive)

Contact Information for Business Card

Business logo, business Name (Corvane Supply Inc), Name (Marcus Pellow), Position (President) Address (58 Fernhollow Lane, Brentwood NY 11742), Contact number (Company 1-855-302-4418, Cell 1-631-245-9073, email address (marcus.pellow@corvanesupply.com), URL (www.corvanesupply.com

Requirements
Must have
• Must include Business Colors (Black, Green, Blue, White) see sample website file
Nice to have
• emboss, spot uv, etc

```html
<!DOCTYPE html>
<html lang="en">
<head>
<meta charset="utf-8">
<title>Corvane Supply – Business Card</title>
<link href="https://fonts.googleapis.com/css2?family=Inter:wght@400;500;600&display=swap" rel="stylesheet">
<style>
  :root {
    --backdrop: #8c8c8c;
    --card: #1c1c1d;
    --brand-blue: #1b2fe8;
    --white: #ffffff;
    --emboss: #4a4a4c;
  }
  * { margin: 0; padding: 0; box-sizing: border-box; }
  html, body {
    width: 1200px; height: 1200px; overflow: hidden;
    background: var(--backdrop);
    font-family: "Inter", Arial, sans-serif;
  }
  .canvas { position: relative; width: 1200px; height: 1200px; }
  .card {
    position: absolute; left: 137px; width: 926px; height: 528px;
    background: var(--card);
    border-radius: 56px 0 56px 0;
    box-shadow: 0 10px 24px rgba(0,0,0,0.35);
  }
  .card--front { top: 53px; }
  .card--back { top: 619px; }

  .brand {
    position: absolute; display: flex; align-items: center; gap: 14px;
    font-weight: 500; white-space: nowrap;
  }
  .brand__dot { border-radius: 50%; flex: none; }
  .card--front .brand { left: 36px; top: 240px; width: 386px; justify-content: center; }
  .card--front .brand__name { color: var(--white); font-size: 38px; }
  .card--front .brand__dot { width: 30px; height: 30px; background: var(--brand-blue); }

  .divider {
    position: absolute; left: 422px; top: 135px; width: 2px; height: 265px;
    background: var(--brand-blue);
  }
  .contact { position: absolute; left: 465px; top: 125px; color: var(--white); }
  .contact__name {
    color: var(--brand-blue); font-size: 40px; font-weight: 600;
    text-transform: uppercase; letter-spacing: 0.5px; line-height: 1;
  }
  .contact__role { font-size: 22px; margin-top: 8px; }
  .contact__address { font-size: 22px; line-height: 31px; margin-top: 12px; }
  .contact__list { list-style: none; margin-top: 12px; }
  .contact__item {
    display: flex; align-items: center; gap: 8px;
    font-size: 22px; line-height: 30.5px;
  }
  .contact__icon { width: 16px; height: 16px; flex: none; }

  .card--back .brand { left: 0; width: 926px; top: 235px; justify-content: center; gap: 20px; }
  .card--back .brand__name { color: var(--emboss); font-size: 62px; }
  .card--back .brand__dot { width: 46px; height: 46px; background: var(--emboss); }
</style>
</head>
<body>
<main class="canvas">
  <section class="card card--front">
    <div class="brand">
      <span class="brand__dot"></span>
      <span class="brand__name">Corvane Supply</span>
    </div>
    <div class="divider"></div>
    <div class="contact">
      <h1 class="contact__name">Marcus Pellow</h1>
      <p class="contact__role">President</p>
      <p class="contact__address">58 Fernhollow Lane,<br>Brentwood NY 11742</p>
      <ul class="contact__list">
        <li class="contact__item">
          <svg class="contact__icon" viewBox="0 0 16 16"><path d="M4 1.5l2.5 3-1.5 1.5c.8 2 2.5 3.7 4.5 4.5L11 9l3 2.5-1.5 2.5C7.5 14 2 8.5 1.5 3z" fill="none" stroke="#1b2fe8" stroke-width="1.4" stroke-linejoin="round"/></svg>
          1-855-302-4418
        </li>
        <li class="contact__item">
          <svg class="contact__icon" viewBox="0 0 16 16"><rect x="4" y="1" width="8" height="14" rx="1.5" fill="none" stroke="#1b2fe8" stroke-width="1.4"/><circle cx="8" cy="12.5" r="0.9" fill="#1b2fe8"/></svg>
          1-631-245-9073
        </li>
        <li class="contact__item">
          <svg class="contact__icon" viewBox="0 0 16 16"><rect x="1.5" y="3.5" width="13" height="9" rx="1" fill="none" stroke="#1b2fe8" stroke-width="1.4"/><path d="M1.8 4l6.2 5 6.2-5" fill="none" stroke="#1b2fe8" stroke-width="1.4"/></svg>
          marcus.pellow@corvanesupply.com
        </li>
        <li class="contact__item">
          <svg class="contact__icon" viewBox="0 0 16 16"><circle cx="8" cy="8" r="6.5" fill="none" stroke="#1b2fe8" stroke-width="1.3"/><ellipse cx="8" cy="8" rx="2.8" ry="6.5" fill="none" stroke="#1b2fe8" stroke-width="1.2"/><path d="M1.5 8h13" stroke="#1b2fe8" stroke-width="1.2"/></svg>
          www.corvanesupply.com
        </li>
      </ul>
    </div>
  </section>

  <section class="card card--back">
    <div class="brand">
      <span class="brand__dot"></span>
      <span class="brand__name">Corvane Supply</span>
    </div>
  </section>
</main>
</body>
</html>
```